Riverbend Heights (by the numbers)

We (city communications office of Riverbend Heights, Arkansas) are launching a magazine to be delivered to every house in the community. We would like the first inside page to be an infographic of the important and interesting "numbers" from 2017. We want it to be visually interesting and convey the huge amount of important services we provide our residents. I have included a document with the relevant statistics to be used.

Target Market(s)

Residents of our city

Industry/Entity Type

House

Colors

Designer to choose colors to be used in the design.

Requirements
Must have
• Our logo must be prominent. The dimensions should be able to fit onto a standard full page magazine. If the infographic is best displayed on two pages we will accept that as well, and change our layout.
Nice to have
• Not every statistic we have provided must be used but if they can be, that is preferable. I have also included some inspirational infographics that appealed to me and inspired the idea, but I am excited about new concepts that might not look anything like those that I have provided.
Should not have
• The design should not have anything incorporated that cannot be presented to families in our community. It must be all ages friendly.

```html
<!DOCTYPE html>
<html lang="en">
<head>
<meta charset="utf-8">
<title>Riverbend Heights by the Numbers</title>
<link rel="stylesheet" href="https://fonts.googleapis.com/css2?family=Open+Sans:wght@300;400;600&display=swap">
<style>
  :root {
    --frame-blue: #1f6cb8;
    --title-white: #ffffff;
    --cell-white: #ffffff;
    --ink: #1f1f1f;
    --sky: #cfe9f7;
    --grass: #8ccb52;
    --grass-deep: #5fae36;
    --sand: #f3dcae;
    --lake: #9fd0e6;
    --road: #9aa1a8;
    --truck-yellow: #f5c623;
    --garbage-green: #4f9a46;
    --tire-black: #333333;
    --leaf-orange: #e9953a;
    --siren-red: #dc3b30;
    --police-black: #2b2b2b;
    --crowd-pink: #f4c4b2;
    --crowd-blue: #a9c9ec;
    --crowd-gold: #f2d58a;
    --brick: #e9b06a;
  }
  * { margin: 0; padding: 0; box-sizing: border-box; }
  html, body { width: 1200px; height: 861px; overflow: hidden; background: #ffffff; }
  body { font-family: "Open Sans", sans-serif; color: var(--ink); }

  .infographic {
    width: 1200px; height: 861px;
    background: var(--frame-blue);
    padding: 0 10px 10px;
    display: grid;
    grid-template-columns: repeat(4, 1fr);
    grid-template-rows: 60px 218px 252px 289px;
    gap: 12px;
  }

  .title-band {
    grid-column: 1 / -1;
    display: flex;
    align-items: center;
    justify-content: space-around;
    color: var(--title-white);
    font-weight: 600;
    font-size: 30px;
    letter-spacing: 0.5px;
  }

  .stat-cell {
    position: relative;
    background: var(--cell-white);
    overflow: hidden;
  }
  .stat-head {
    position: relative;
    z-index: 1;
    display: flex;
    justify-content: space-between;
    align-items: flex-start;
    padding: 12px 14px 0;
    gap: 8px;
  }
  .stat-label { font-size: 14px; line-height: 1.25; font-weight: 400; max-width: 118px; }
  .stat-value { font-size: 34px; font-weight: 300; line-height: 1; white-space: nowrap; }

  .stat-art {
    position: absolute;
    left: 0; right: 0; bottom: 0;
    top: 40%;
  }
  .stat-cell.tall-label .stat-art { top: 48%; }

  .art-population {
    background:
      radial-gradient(ellipse 40% 30% at 30% 45%, var(--crowd-pink), transparent 70%),
      radial-gradient(ellipse 40% 30% at 65% 55%, var(--crowd-blue), transparent 70%),
      radial-gradient(ellipse 45% 30% at 45% 80%, var(--crowd-gold), transparent 70%),
      #ffffff;
  }
  .art-park-visitors {
    background:
      radial-gradient(ellipse 35% 25% at 50% 62%, #c99a63, transparent 75%),
      linear-gradient(180deg, var(--sky) 0%, var(--grass) 40%, var(--lake) 62%, var(--sand) 100%);
  }
  .art-police {
    background:
      radial-gradient(ellipse 42% 30% at 50% 55%, var(--police-black), transparent 75%),
      radial-gradient(ellipse 22% 14% at 50% 55%, #f4f4f4, transparent 80%),
      #ffffff;
  }
  .art-fire {
    background:
      radial-gradient(ellipse 45% 32% at 50% 55%, var(--siren-red), transparent 75%),
      radial-gradient(ellipse 30% 10% at 50% 85%, #555555, transparent 80%),
      #ffffff;
  }
  .art-asphalt {
    background:
      radial-gradient(ellipse 35% 28% at 55% 58%, var(--truck-yellow), transparent 75%),
      radial-gradient(ellipse 30% 22% at 38% 62%, #4a5a66, transparent 75%),
      linear-gradient(180deg, #ffffff 0%, #eef0f2 70%, var(--road) 100%);
  }
  .art-garbage {
    background:
      radial-gradient(ellipse 42% 30% at 48% 52%, var(--garbage-green), transparent 75%),
      radial-gradient(ellipse 14% 14% at 80% 78%, #3e8ccc, transparent 80%),
      linear-gradient(180deg, #ffffff 0%, #f2f4f2 100%);
  }
  .art-tires {
    background:
      radial-gradient(ellipse 30% 38% at 50% 52%, var(--tire-black), transparent 72%),
      #ffffff;
  }
  .art-yard {
    background:
      radial-gradient(ellipse 30% 25% at 40% 35%, var(--leaf-orange), transparent 75%),
      radial-gradient(ellipse 30% 22% at 50% 78%, var(--garbage-green), transparent 75%),
      #ffffff;
  }
  .art-parks {
    background:
      radial-gradient(ellipse 25% 18% at 78% 20%, var(--grass-deep), transparent 75%),
      radial-gradient(ellipse 22% 14% at 40% 55%, #f3f3f0, transparent 80%),
      linear-gradient(180deg, #f3f9ec 0%, var(--grass) 55%, var(--grass-deep) 100%);
  }
  .art-playground {
    background:
      radial-gradient(ellipse 28% 25% at 38% 55%, var(--leaf-orange), transparent 75%),
      radial-gradient(ellipse 20% 20% at 70% 48%, var(--siren-red), transparent 75%),
      linear-gradient(180deg, #ffffff 0%, #ffffff 60%, var(--grass) 100%);
  }

  .city-cell {
    grid-column: 2 / 4;
    position: relative;
    display: flex;
    align-items: center;
    justify-content: center;
    background:
      radial-gradient(ellipse 18% 40% at 18% 62%, #3f6fb0, transparent 75%),
      radial-gradient(ellipse 16% 35% at 82% 60%, var(--brick), transparent 75%),
      radial-gradient(ellipse 12% 30% at 92% 70%, #3f8a3a, transparent 75%),
      linear-gradient(180deg, var(--sky) 0%, #e1f2fb 55%, #a9b6c4 85%, var(--road) 100%);
  }
  .city-name-plate {
    background: var(--cell-white);
    padding: 18px 28px;
    display: flex;
    align-items: center;
    gap: 14px;
  }
  .city-name-mark { width: 34px; height: 34px; border-radius: 50%; background: var(--frame-blue); }
  .city-name { color: var(--frame-blue); font-weight: 600; font-size: 34px; line-height: 1; }
</style>
</head>
<body>
<main class="infographic">
  <header class="title-band">
    <span class="title-part">Riverbend Heights (RBH)</span>
    <span class="title-part">by the Numbers (#'s)</span>
  </header>

  <section class="stat-cell">
    <div class="stat-head"><p class="stat-label">Population</p><p class="stat-value">65,004</p></div>
    <div class="stat-art art-population" role="img" aria-label="Illustration of a crowd of residents"></div>
  </section>
  <section class="stat-cell">
    <div class="stat-head"><p class="stat-label">Visitors to Cedar Hollow Park</p><p class="stat-value">779,621</p></div>
    <div class="stat-art art-park-visitors" role="img" aria-label="Illustration of a wooden park bench by a lake"></div>
  </section>
  <section class="stat-cell">
    <div class="stat-head"><p class="stat-label">Police 911 calls</p><p class="stat-value">26,660</p></div>
    <div class="stat-art art-police" role="img" aria-label="Illustration of a police car"></div>
  </section>
  <section class="stat-cell">
    <div class="stat-head"><p class="stat-label">Fire 911 calls</p><p class="stat-value">12,560</p></div>
    <div class="stat-art art-fire" role="img" aria-label="Illustration of a red fire truck"></div>
  </section>

  <section class="stat-cell tall-label">
    <div class="stat-head"><p class="stat-label">Tons of asphalt used in repairing potholes and street overlays</p><p class="stat-value">5,952</p></div>
    <div class="stat-art art-asphalt" role="img" aria-label="Illustration of a yellow dump truck with road cones"></div>
  </section>
  <section class="stat-cell">
    <div class="stat-head"><p class="stat-label">Tons of Household garbage collected</p><p class="stat-value">16,768</p></div>
    <div class="stat-art art-garbage" role="img" aria-label="Illustration of a green garbage truck and bins"></div>
  </section>
  <section class="stat-cell">
    <div class="stat-head"><p class="stat-label">Used tires recycled</p><p class="stat-value">4,221</p></div>
    <div class="stat-art art-tires" role="img" aria-label="Illustration of a stack of used tires"></div>
  </section>
  <section class="stat-cell">
    <div class="stat-head"><p class="stat-label">Cubic yards of green (yard) waste collected</p><p class="stat-value">116,675</p></div>
    <div class="stat-art art-yard" role="img" aria-label="Illustration of autumn leaves falling into a green recycling bin"></div>
  </section>

  <section class="stat-cell">
    <div class="stat-head"><p class="stat-label">Neighborhood parks</p><p class="stat-value">34</p></div>
    <div class="stat-art art-parks" role="img" aria-label="Illustration of a park with a bench, trees and lamp post"></div>
  </section>
  <section class="city-cell" role="img" aria-label="Illustration of the city skyline with buildings, a bus and a car">
    <div class="city-name-plate">
      <span class="city-name-mark"></span>
      <span class="city-name">Riverbend Heights</span>
    </div>
  </section>
  <section class="stat-cell tall-label">
    <div class="stat-head"><p class="stat-label">Open Arms Inclusive Playgrounds built for kids with special needs</p><p class="stat-value">1</p></div>
    <div class="stat-art art-playground" role="img" aria-label="Illustration of a playground with swings and a slide"></div>
  </section>
</main>
</body>
</html>
```